Global Expert Network Firm needs business card design

We need business card design for a new company based in Seoul, South Korea called 'Corwell Insight Partners'. We recruit industry experts covering all countries and connect our client and recruited expert by phone, face-to-face meetings and etc. We are a global expert network firm that is focused on delivering high-quality experts to our clients throughout the world. Our clients include multinational corporations, global consulting firms, private equity firms, venture capital firms, asset management companies.
We have made new logo and please find attachment.(Please use new logo)
Target Market(s)
Global Consulting Firms, Investment Firms, Private Equity Firms, Venture Capital Firms.
Industry/Entity Type
Recruitment
Contact Information for Business Card
We need two Languages (English and Korean Version).
The front is Korean and the back is English version.
[The back] [English]
Company Name: Corwell Insight Partners, Inc.
CEO Name: Daniel Park
Address: #507, Hanbit Bldg, 82 Maebongsan-ro, Dobong-gu, Seoul, 01327, Korea
Tel. +82 2 718 4052
Fax. +82 2 864 1097
Mobile. +82 10 7264 8815
Email: daniel@corwellip.com
Web: www.corwellip.com
[The front] [Korean] => Described in same order as English version.
회사명: 코웰인사이트파트너스(주)
대표이사: 박도현
주소: 서울시 도봉구 매봉산로 82 한빛빌딩 507호
Tel. 02 718 4052
Fax. 02 864 1097
Mobile. 010 7264 8815
Web: www.corwellip.com
Look and feel
Each slider illustrates characteristics of the customer's brand and the style your logo design should communicate.

```html
<!DOCTYPE html>
<html lang="en">
<head>
<meta charset="utf-8">
<title>Corwell Insight Partners — Business Cards</title>
<link rel="stylesheet" href="https://fonts.googleapis.com/css2?family=Marcellus&family=Questrial&family=Nanum+Myeongjo:wght@400;700&display=swap">
<style>
  :root {
    --navy: #1d2252;
    --navy-deep: #1b1f4f;
    --paper: #ffffff;
    --ink: #1d2252;
    --shadow: rgba(5, 8, 30, 0.55);
  }
  * { box-sizing: border-box; margin: 0; padding: 0; }
  html, body { width: 1200px; height: 1200px; overflow: hidden; }
  body { background: var(--navy-deep); position: relative; font-family: "Questrial", sans-serif; }

  .card {
    position: absolute;
    width: 664px;
    height: 398px;
    overflow: hidden;
    box-shadow: 0 10px 22px var(--shadow);
  }
  .card--english { left: 272px; top: 154px; border-radius: 8px 20px 20px 20px; background: var(--paper); }
  .card--korean  { left: 274px; top: 662px; border-radius: 40px 16px 16px 40px; background: var(--navy); }

  .panel { position: absolute; top: 0; bottom: 0; }
  .card--english .panel--brand { left: 0; width: 370px; background: var(--navy); }
  .card--english .tab { position: absolute; left: 370px; top: 146px; width: 12px; height: 110px; background: var(--navy); }
  .card--korean .panel--brand { left: 0; width: 338px; background: var(--paper); }
  .card--korean .tab { position: absolute; left: 338px; top: 148px; width: 6px; height: 110px; background: var(--paper); }

  .wordmark {
    position: absolute; left: 40px; top: 36px;
    font-family: "Marcellus", serif; font-size: 33px; line-height: 45px; letter-spacing: 0.5px;
  }
  .card--english .wordmark, .card--english .tagline, .card--english .address { color: var(--paper); }
  .card--korean .wordmark, .card--korean .tagline, .card--korean .address { color: var(--ink); }

  .tagline {
    position: absolute; left: 40px; top: 202px;
    font-size: 6px; letter-spacing: 1.4px; text-transform: uppercase;
  }

  .address {
    position: absolute; left: 40px; font-size: 14px; line-height: 22px;
  }
  .card--english .address { top: 304px; }
  .card--korean .address { top: 306px; font-family: "Nanum Myeongjo", serif; font-size: 19px; line-height: 25px; }
  .address .pin { display: inline-block; width: 9px; height: 12px; vertical-align: -1px; margin-right: 2px; }
  .card--korean .address .indent { padding-left: 14px; }

  .identity { position: absolute; right: 42px; top: 36px; text-align: right; }
  .card--english .identity { color: var(--ink); }
  .card--korean .identity { color: var(--paper); right: 40px; }
  .identity .name { font-size: 29px; line-height: 34px; }
  .card--korean .identity .name { font-family: "Nanum Myeongjo", serif; font-size: 22px; line-height: 30px; }

  .identity .title-line {
    display: flex; justify-content: flex-end; align-items: center;
    gap: 8px; margin-top: 2px;
  }
  .identity .rule { height: 1px; flex: none; }
  .card--english .identity .rule { width: 128px; background: var(--ink); }
  .card--korean .identity .rule { width: 176px; background: var(--paper); }
  .identity .role { font-size: 12px; line-height: 14px; padding-top: 10px; }
  .card--korean .identity .role { font-family: "Nanum Myeongjo", serif; font-size: 16px; line-height: 18px; padding-top: 14px; }

  .contacts { position: absolute; right: 40px; top: 202px; list-style: none; }
  .card--english .contacts { color: var(--ink); }
  .card--korean .contacts { color: var(--paper); }
  .contacts li { height: 32px; font-size: 14px; display: flex; justify-content: flex-end; align-items: center; gap: 8px; }
  .contacts svg { width: 12px; height: 12px; flex: none; }
</style>
</head>
<body>

<svg width="0" height="0" style="position:absolute">
  <defs>
    <symbol id="icon-phone" viewBox="0 0 12 12"><path d="M2.5 1l2 2.2-1 1.2c.7 1.5 1.6 2.4 3.1 3.1l1.2-1 2.2 2-1.2 1.9C5.5 10.2 1.8 6.5 1 2.2z" fill="currentColor"/></symbol>
    <symbol id="icon-fax" viewBox="0 0 12 12"><path d="M1 6.5c0-2 2.3-3 5-3s5 1 5 3l-.5 1.5H8.5V6.5h-5V8H1.5z" fill="currentColor"/></symbol>
    <symbol id="icon-mobile" viewBox="0 0 12 12"><rect x="3.5" y="1" width="5" height="10" rx="1" fill="none" stroke="currentColor" stroke-width="1.2"/><rect x="5.3" y="9" width="1.4" height="1" fill="currentColor"/></symbol>
    <symbol id="icon-mail" viewBox="0 0 12 12"><rect x="1" y="3" width="10" height="7" rx="0.8" fill="currentColor"/></symbol>
    <symbol id="icon-web" viewBox="0 0 12 12"><circle cx="6" cy="6" r="4.6" fill="none" stroke="currentColor" stroke-width="1.1"/><path d="M1.5 6h9M6 1.4c-2 2.6-2 6.6 0 9.2M6 1.4c2 2.6 2 6.6 0 9.2" fill="none" stroke="currentColor" stroke-width="0.9"/></symbol>
    <symbol id="icon-pin" viewBox="0 0 9 12"><path d="M4.5 0A4 4 0 0 0 .5 4c0 3 4 8 4 8s4-5 4-8a4 4 0 0 0-4-4zm0 5.6a1.6 1.6 0 1 1 0-3.2 1.6 1.6 0 0 1 0 3.2z" fill="currentColor"/></symbol>
  </defs>
</svg>

<section class="card card--english" aria-label="Business card, English side">
  <div class="panel panel--brand"></div>
  <div class="tab"></div>
  <div class="wordmark">CORWELL<br>INSIGHT<br>PARTNERS</div>
  <div class="tagline">Expert insight. Worldwide.</div>
  <p class="address"><svg class="pin"><use href="#icon-pin"/></svg>#507, Hanbit Bldg, 82 Maebongsan-ro,<br>Dobong-gu, Seoul, 01327, Korea</p>

  <div class="identity">
    <div class="name">Daniel Park</div>
    <div class="title-line">
      <div class="rule"></div>
      <div class="role">CEO</div>
    </div>
  </div>
  <ul class="contacts">
    <li>+82 2 718 4052 <svg><use href="#icon-phone"/></svg></li>
    <li>+82 2 864 1097 <svg><use href="#icon-fax"/></svg></li>
    <li>+82 10 7264 8815 <svg><use href="#icon-mobile"/></svg></li>
    <li>daniel@corwellip.com <svg><use href="#icon-mail"/></svg></li>
    <li>www.corwellip.com <svg><use href="#icon-web"/></svg></li>
  </ul>
</section>

<section class="card card--korean" aria-label="Business card, Korean side" lang="ko">
  <div class="panel panel--brand"></div>
  <div class="tab"></div>
  <div class="wordmark" lang="en">CORWELL<br>INSIGHT<br>PARTNERS</div>
  <div class="tagline" lang="en">Expert insight. Worldwide.</div>
  <p class="address"><svg class="pin"><use href="#icon-pin"/></svg>서울시 도봉구 매봉산로<br><span class="indent">82 한빛빌딩 507호</span></p>

  <div class="identity">
    <div class="name">코웰인사이트파트너스(주)</div>
    <div class="title-line">
      <div class="rule"></div>
      <div class="role">박도현</div>
    </div>
  </div>
  <ul class="contacts">
    <li>+82 2 718 4052 <svg><use href="#icon-phone"/></svg></li>
    <li>+82 2 864 1097 <svg><use href="#icon-fax"/></svg></li>
    <li>+82 10 7264 8815 <svg><use href="#icon-mobile"/></svg></li>
    <li>daniel@corwellip.com <svg><use href="#icon-mail"/></svg></li>
    <li>www.corwellip.com <svg><use href="#icon-web"/></svg></li>
  </ul>
</section>

</body>
</html>
```